Business Card, A4 Letter Head and DL Envelope for Brandolux

We are looking for a design for our Business Card, A4 Letter Head and DL Envelope.

Brandolux is a distributor of promotional products. We specialize in a range of branded promotional products, these include pens, polo shirts, key rings, drink bottles, uniforms and bags to name a few. We are experts in marketing and assist companies in choosing the right promotional product for their needs. We will predominately be an online business where customers visit our website and browse our range of promotional products and branding options.

Our colours are black, red, white and grey.

Files must be supplied in eps, pdf and ai format.

Please display the following information:
Dorian Pell
Account Manager
Suite xxx, 214 Harwick Lane Melbourne, Victoria 3000
Phone +61 3 5550 1842
Mobile +61 455 501 736
sales@brandolux.example
www.brandolux.example

```html
<!DOCTYPE html>
<html lang="en">
<head>
<meta charset="utf-8">
<title>Brandolux DL Envelope</title>
<link rel="stylesheet" href="https://fonts.googleapis.com/css2?family=Questrial&display=swap">
<style>
  :root {
    --stage: #6b6b6b;
    --paper: #ffffff;
    --red: #d71d24;
    --red-deep: #bd1b22;
    --ink: #1a1a1a;
    --grey: #8a8a8a;
    --faint: #efefef;
  }
  * { margin: 0; padding: 0; box-sizing: border-box; }
  html, body {
    width: 1200px; height: 1110px; overflow: hidden;
    background: radial-gradient(ellipse at 50% 45%, #7a7a7a 0%, var(--stage) 70%);
    font-family: "Questrial", sans-serif;
  }
  .envelope {
    position: absolute; left: 125px; width: 960px; height: 419px;
    background: var(--paper);
    box-shadow: 0 4px 8px rgba(0,0,0,.35);
    overflow: hidden;
  }
  .envelope--front { top: 52px; }
  .envelope--back { top: 613px; }
  .band { position: absolute; display: block; }
  .front-top-band { left: 368px; top: 0; width: 592px; height: 75px; }
  .front-bottom-band { left: 0; bottom: 0; width: 960px; height: 14px; }
  .back-flap { left: 0; top: 0; width: 960px; height: 75px; }
  .back-bottom-band { left: 0; bottom: 0; width: 960px; height: 26px; }

  .brand {
    position: absolute; left: 62px; top: 15px;
    display: flex; align-items: center; gap: 12px;
  }
  .brand-dot {
    width: 54px; height: 54px; border-radius: 50%;
    background: var(--red);
  }
  .brand-name {
    font-size: 26px; letter-spacing: .5px; color: var(--ink);
  }
  .contact {
    position: absolute; left: 64px; top: 94px;
    border-left: 1px solid #9a9a9a;
    padding-left: 8px;
    font-size: 10.5px; line-height: 13.5px; color: var(--ink);
  }
  .contact-label { color: var(--red); display: inline-block; width: 12px; }
  .contact-address { color: var(--red); }
  .faint-mark {
    position: absolute; left: 779px; top: 239px;
    width: 125px; height: 125px; border-radius: 50%;
    background: var(--faint);
  }
</style>
</head>
<body>
  <section class="envelope envelope--front" aria-label="DL envelope front">
    <svg class="band front-top-band" viewBox="0 0 592 75" preserveAspectRatio="none">
      <rect width="592" height="75" fill="var(--red)"/>
      <path d="M0 0 H592 V72 C420 30 200 12 0 12 Z" fill="var(--red-deep)"/>
    </svg>
    <div class="brand">
      <span class="brand-dot"></span>
      <span class="brand-name">BRANDOLUX</span>
    </div>
    <div class="contact">
      <div><span class="contact-label">M</span>+61 455 501 736</div>
      <div><span class="contact-label">T</span>+61 3 5550 1842</div>
      <div><span class="contact-label">e</span>sales@brandolux.example</div>
      <div class="contact-address">Suite xxx, 214 Harwick Lane</div>
      <div class="contact-address">Melbourne, Victoria 3000</div>
    </div>
    <div class="faint-mark"></div>
    <svg class="band front-bottom-band" viewBox="0 0 960 14" preserveAspectRatio="none">
      <rect width="960" height="14" fill="var(--red)"/>
      <path d="M0 0 H960 V3 C600 4 300 9 0 7 Z" fill="var(--red-deep)"/>
    </svg>
  </section>

  <section class="envelope envelope--back" aria-label="DL envelope back">
    <svg class="band back-flap" viewBox="0 0 960 75">
      <path d="M0 0 H960 V47 A28 28 0 0 1 932 75 H28 A28 28 0 0 1 0 47 Z" fill="var(--red)"/>
      <path d="M0 0 H960 V14 C700 12 380 22 0 55 Z" fill="var(--red-deep)"/>
    </svg>
    <svg class="band back-bottom-band" viewBox="0 0 960 26">
      <path d="M0 26 V26 A26 26 0 0 1 26 0 H934 A26 26 0 0 1 960 26 Z" fill="var(--red-deep)"/>
    </svg>
  </section>
</body>
</html>
```